TRLV EDonult data- General and Cardiology

We are a department within the University of Brekmoor that does research and focuses on electronic asynchronous consultations (eConsults) between primary care physicians and specialty physicians. We have data about use of eConsults in rural and frontier areas and need graphical representation of the data. Would appreciate having a meeting with the designer that gets assigned to this project to talk about vision and requirements, if possible.

Target Market(s)

targets are for federal research grants and within University sharing

Font styles to use
Other font styles liked:
• Arial

Requirements
Must have
• Different graphic for cardiology specific and total EConsults across all specialties using same graphic model.
Nice to have
• Clear distinction between urban. served and underserved rural areas.
Should not have
• uneccesary images

```html
<!DOCTYPE html>
<html lang="en">
<head>
<meta charset="utf-8">
<title>eConsults Utilization in Rural and Frontier Areas</title>
<link href="https://fonts.googleapis.com/css2?family=Archivo+Black&family=Arimo:ital,wght@0,400;0,700;1,400&display=swap" rel="stylesheet">
<style>
:root{
  --teal:#236272;
  --orange:#f07d4f;
  --tier1:#f07d4f;
  --tier2:#f39b77;
  --tier3:#f5c6b1;
  --tier4:#fce3d8;
  --none:#a8a9ac;
  --bg:#f0f0f0;
  --white:#ffffff;
  --ink:#222222;
  --card-line:#f6c9b6;
}
*{box-sizing:border-box;margin:0;padding:0}
html,body{width:1200px;height:720px;overflow:hidden;background:var(--bg)}
body{position:relative;font-family:"Arimo",Arial,sans-serif;color:var(--ink)}
.abs{position:absolute}
.heavy{font-family:"Archivo Black","Arial Black",sans-serif}

.title-band{left:0;top:0;width:618px;height:95px;background:var(--teal)}
.title-line{left:31px;color:var(--white);font-size:30px;letter-spacing:1.2px;line-height:1;white-space:nowrap}
.title-line.one{top:16px}
.title-line.two{top:50px;background:var(--orange);padding:2px 12px 1px 3px;font-size:29.5px}

.map-head{left:618px;top:0;width:582px;height:75px;background:var(--white);text-align:center;color:var(--teal)}
.map-head h2{font-family:"Archivo Black","Arial Black",sans-serif;font-size:18px;line-height:21px;letter-spacing:.8px;margin-top:8px;font-weight:400}
.date-tag{display:inline-block;background:var(--orange);color:var(--white);font-family:"Archivo Black","Arial Black",sans-serif;font-size:18px;line-height:20px;padding:0 10px;letter-spacing:.8px}
.map-band{left:618px;top:75px;width:582px;height:20px;background:var(--orange);color:var(--white);text-align:center;font-weight:700;font-size:16px;line-height:20px;letter-spacing:.5px}

.state-map{left:620px;top:100px;width:534px;height:366px;border:1px solid #e9c9bb;
  background:
    radial-gradient(ellipse 90px 70px at 62% 38%, #f07d4f 0%, rgba(240,125,79,.85) 45%, rgba(240,125,79,0) 100%),
    radial-gradient(ellipse 70px 60px at 66% 58%, rgba(240,125,79,.9) 0%, rgba(240,125,79,0) 100%),
    radial-gradient(ellipse 110px 60px at 60% 12%, rgba(243,155,119,.9) 0%, rgba(243,155,119,0) 100%),
    radial-gradient(ellipse 60px 40px at 12% 82%, rgba(168,169,172,.9) 0%, rgba(168,169,172,0) 100%),
    radial-gradient(ellipse 50px 50px at 88% 60%, rgba(168,169,172,.85) 0%, rgba(168,169,172,0) 100%),
    radial-gradient(ellipse 40px 40px at 40% 12%, rgba(168,169,172,.85) 0%, rgba(168,169,172,0) 100%),
    linear-gradient(135deg,#fbe0d4,#f8d3c2 55%,#fce3d8)}
.wedge{left:470px;top:100px}
.us-map{left:345px;top:182px;width:260px;height:150px;border-radius:40px 30px 60px 50px;background:linear-gradient(90deg,#236272,#3d6f79 70%,#5b7d84)}

.section-tab{left:0;background:var(--teal);color:var(--white);font-family:"Archivo Black","Arial Black",sans-serif;letter-spacing:.4px;padding-left:31px;border-radius:0 3px 3px 0;white-space:nowrap;overflow:hidden}
.tab-all{top:121px;width:418px;height:37px;line-height:37px;font-size:15.5px}
.tab-urban{top:314px;width:380px;height:29px;line-height:30px;font-size:15.5px}

.card{background:var(--white);border:1px solid var(--card-line);border-radius:5px}
.total-card{left:20px;top:171px;width:290px;height:130px}
.doctor-art{left:27px;top:175px;width:143px;height:118px;background:linear-gradient(160deg,#cfe7ee,#3f6f7c);border-radius:6px}
.total-label{left:190px;top:193px;color:var(--teal);font-weight:700;font-size:17px;line-height:20px;letter-spacing:.5px}
.total-value{left:190px;top:254px;color:var(--orange);font-family:"Archivo Black","Arial Black",sans-serif;font-size:31px;letter-spacing:1px}

.share-card{top:355px;height:83px}
.share-card.urban{left:20px;width:246px}
.share-card.rural{left:277px;width:245px}
.share-icon{top:365px;width:68px;height:66px;border-radius:4px}
.share-icon.city{left:32px;background:linear-gradient(180deg,#f3a07c,#236272 60%)}
.share-icon.home{left:291px;background:linear-gradient(180deg,#dfe9ec,#236272 55%,#f07d4f)}
.share-pct{color:var(--orange);font-family:"Archivo Black","Arial Black",sans-serif;font-size:25px;top:360px}
.share-text{font-size:9.4px;font-weight:700;line-height:11.6px;top:394px;color:#2b2b2b;white-space:nowrap}
.footnote{left:387px;top:445px;font-size:6.2px;font-style:italic;line-height:7.6px;color:#444}

.county-band{left:0;top:466px;width:1200px;height:29px;background:var(--teal);color:var(--white);text-align:center;font-weight:700;font-size:20px;line-height:30px;letter-spacing:.8px}

.legend{left:20px;top:507px;width:270px;height:193px;background:#f8f8f8;box-shadow:0 0 3px rgba(0,0,0,.08)}
.legend-row{position:absolute;left:15px;width:240px;height:24px}
.legend-swatch{position:absolute;left:0;top:0;width:143px;height:24px}
.legend-label{position:absolute;left:152px;width:88px;text-align:center;font-weight:700;font-size:14px;line-height:24px}

.t1{background:var(--tier1)}.t2{background:var(--tier2)}.t3{background:var(--tier3)}.t4{background:var(--tier4)}.t0{background:var(--none)}

.table{background:var(--white);box-shadow:0 0 3px rgba(0,0,0,.08)}
.table-head{background:var(--teal);color:var(--white);text-align:center;font-weight:700;font-size:15.5px;letter-spacing:.4px}
.urban-table{left:309px;top:507px;width:271px;height:195px}
.urban-table .table-head{height:21px;line-height:22px}
.rural-table{left:602px;top:508px;width:570px;height:194px}
.rural-table .table-head{height:22px;line-height:23px}
.cols{display:flex;height:calc(100% - 22px)}
.col{flex:1;padding:7px 0 0;border-left:1px solid #555}
.col:first-child{border-left:none}
.row{display:flex;align-items:center;height:17.8px;font-size:10px;padding:0 12px 0 13px;white-space:nowrap}
.row i{width:7px;height:7px;margin-right:9px;flex:none}
.row span{flex:1}
.row b{font-weight:400;text-align:right}
</style>
</head>
<body>

<div class="abs title-band"></div>
<div class="abs heavy title-line one">ECONSULTS UTILIZATION IN</div>
<div class="abs heavy title-line two">RURAL AND FRONTIER AREAS</div>

<div class="abs map-head">
  <h2>DISTRIBUTION OF ECONSULTS BY COUNTY<br>AND RURALITY ALL SPECIALTIES</h2>
  <span class="date-tag">2018 - JANUARY 2024</span>
</div>
<div class="abs map-band">COLORADO MAP</div>

<svg class="abs wedge" width="150" height="366" viewBox="0 0 150 366" aria-hidden="true">
  <polygon points="0,145 150,0 150,366 0,170" fill="#f3ddd4" opacity=".7"/>
</svg>
<div class="abs us-map" role="img" aria-label="Map of the United States with Colorado highlighted in orange"></div>
<div class="abs state-map" role="img" aria-label="Colorado county map shaded by number of eConsults ordered: Denver metro and Front Range counties in dark orange (over 1000), northern counties in medium orange, most rural and frontier counties in light peach, and counties with no eConsults in grey"></div>

<div class="abs section-tab tab-all">ECONSULTS ACROSS ALL SPECIALTIES</div>
<div class="abs card total-card"></div>
<div class="abs doctor-art" role="img" aria-label="Illustration of a doctor on a laptop screen beside a medical kit"></div>
<div class="abs total-label">TOTAL<br>ECONSULTS<br>ORDERED</div>
<div class="abs total-value">21967</div>

<div class="abs section-tab tab-urban">URBAN VS. RURAL DISTRIBUTION</div>
<div class="abs card share-card urban"></div>
<div class="abs share-icon city" role="img" aria-label="City buildings icon"></div>
<div class="abs share-pct" style="left:112px">97%</div>
<div class="abs share-text" style="left:112px">of eConsults ordered across<br>all specialties were for patients<br>in urban counties statewide</div>

<div class="abs card share-card rural"></div>
<div class="abs share-icon home" role="img" aria-label="Rural house with trees icon"></div>
<div class="abs share-pct" style="left:371px">1%</div>
<div class="abs share-text" style="left:371px">of eConsults ordered across all<br>specialties were for rural and<br>frontier counties combined</div>
<div class="abs footnote">*2% of eConsults ordered across all specialties<br>were for patients out-of-state</div>

<div class="abs county-band">DISTRIBUTION OF ECONSULTS BY COUNTY</div>

<div class="abs legend">
  <div class="legend-row" style="top:15px"><div class="legend-swatch t1"></div><div class="legend-label">6000-1000</div></div>
  <div class="legend-row" style="top:49px"><div class="legend-swatch t2"></div><div class="legend-label">1000-100</div></div>
  <div class="legend-row" style="top:84px"><div class="legend-swatch t3"></div><div class="legend-label">100-10</div></div>
  <div class="legend-row" style="top:118px"><div class="legend-swatch t4"></div><div class="legend-label">10-1</div></div>
  <div class="legend-row" style="top:153px"><div class="legend-swatch t0"></div><div class="legend-label">None</div></div>
</div>

<div class="abs table urban-table">
  <div class="table-head">URBAN AREA</div>
  <div class="cols">
    <div class="col">
      <div class="row"><i class="t1"></i><span>Denver</span><b>5749</b></div>
      <div class="row"><i class="t1"></i><span>Arapahoe</span><b>5060</b></div>
      <div class="row"><i class="t1"></i><span>Douglas</span><b>2497</b></div>
      <div class="row"><i class="t1"></i><span>Adams</span><b>2018</b></div>
      <div class="row"><i class="t1"></i><span>El Paso</span><b>1542</b></div>
      <div class="row"><i class="t1"></i><span>Jefferson</span><b>1466</b></div>
      <div class="row"><i class="t1"></i><span>Weld</span><b>998</b></div>
      <div class="row"><i class="t1"></i><span>Larimer</span><b>847</b></div>
      <div class="row"><i class="t1"></i><span>Boulder</span><b>503</b></div>
    </div>
    <div class="col">
      <div class="row"><i class="t2"></i><span>Broomfield</span><b>279</b></div>
      <div class="row"><i class="t2"></i><span>Elbert</span><b>106</b></div>
      <div class="row"><i class="t3"></i><span>Pueblo</span><b>72</b></div>
      <div class="row"><i class="t3"></i><span>Teller</span><b>71</b></div>
      <div class="row"><i class="t3"></i><span>Park</span><b>30</b></div>
      <div class="row"><i class="t3"></i><span>Mesa</span><b>16</b></div>
      <div class="row"><i class="t3"></i><span>Glipin</span><b>12</b></div>
      <div class="row"><i class="t4"></i><span>Clear Creek</span><b>5</b></div>
    </div>
  </div>
</div>

<div class="abs table rural-table">
  <div class="table-head">RURAL/FRONTIER AREA</div>
  <div class="cols">
    <div class="col">
      <div class="row"><i class="t3"></i><span>Morgan</span><b>19</b></div>
      <div class="row"><i class="t3"></i><span>Routt</span><b>19</b></div>
      <div class="row"><i class="t3"></i><span>Eagle</span><b>16</b></div>
      <div class="row"><i class="t3"></i><span>Summit</span><b>15</b></div>
      <div class="row"><i class="t3"></i><span>Fremont</span><b>14</b></div>
      <div class="row"><i class="t3"></i><span>Logan</span><b>13</b></div>
      <div class="row"><i class="t3"></i><span>Chaffee</span><b>12</b></div>
      <div class="row"><i class="t3"></i><span>Grand</span><b>12</b></div>
      <div class="row"><i class="t4"></i><span>Garfield</span><b>9</b></div>
    </div>
    <div class="col">
      <div class="row"><i class="t4"></i><span>Huerfano</span><b>7</b></div>
      <div class="row"><i class="t4"></i><span>Alamosa</span><b>6</b></div>
      <div class="row"><i class="t4"></i><span>Kit Carson</span><b>6</b></div>
      <div class="row"><i class="t4"></i><span>Otero</span><b>6</b></div>
      <div class="row"><i class="t4"></i><span>Lincoln</span><b>5</b></div>
      <div class="row"><i class="t4"></i><span>Delta</span><b>4</b></div>
      <div class="row"><i class="t4"></i><span>Montrose</span><b>4</b></div>
      <div class="row"><i class="t4"></i><span>Pitkin</span><b>4</b></div>
      <div class="row"><i class="t4"></i><span>Bent</span><b>3</b></div>
    </div>
    <div class="col">
      <div class="row"><i class="t4"></i><span>Custer</span><b>3</b></div>
      <div class="row"><i class="t4"></i><span>Las Animas</span><b>3</b></div>
      <div class="row"><i class="t4"></i><span>Moffat</span><b>3</b></div>
      <div class="row"><i class="t4"></i><span>Archuleta</span><b>2</b></div>
      <div class="row"><i class="t4"></i><span>Lake</span><b>2</b></div>
      <div class="row"><i class="t4"></i><span>Montezuma</span><b>2</b></div>
      <div class="row"><i class="t4"></i><span>Prowers</span><b>2</b></div>
      <div class="row"><i class="t4"></i><span>Rio Blanco</span><b>2</b></div>
      <div class="row"><i class="t4"></i><span>Baca</span><b>1</b></div>
    </div>
    <div class="col">
      <div class="row"><i class="t4"></i><span>Costilla</span><b>1</b></div>
      <div class="row"><i class="t4"></i><span>Gunnison</span><b>1</b></div>
      <div class="row"><i class="t4"></i><span>Phillips</span><b>1</b></div>
      <div class="row"><i class="t4"></i><span>Rio Grande</span><b>1</b></div>
      <div class="row"><i class="t4"></i><span>Saguache</span><b>1</b></div>
      <div class="row"><i class="t4"></i><span>San Miguel</span><b>1</b></div>
      <div class="row"><i class="t4"></i><span>Washington</span><b>1</b></div>
      <div class="row"><i class="t4"></i><span>Yuma</span><b>1</b></div>
    </div>
  </div>
</div>

</body>
</html>
```